DH Business Card

I have included previous cards for example and info. New Employee is Derek Halvorsen, Patient Liaison. His cell is 910-555-0143. His email is Derek@tallowmedco.com. I like all the services listed on the back. I like front minimalist design, but needs to have the info somewhere. Three locations and three phone numbers. I have included our brochure showing the three locations for reference.

```html
<!DOCTYPE html>
<html lang="en">
<head>
<meta charset="utf-8">
<title>DH Business Card</title>
<link href="https://fonts.googleapis.com/css2?family=Arimo:wght@400;700&display=swap" rel="stylesheet">
<style>
  :root {
    --brand-blue: #283593;
    --brand-red: #e3141d;
    --paper: #ffffff;
    --ink: #1a1a1a;
    --backdrop: #2a2a2c;
  }
  * { box-sizing: border-box; margin: 0; padding: 0; }
  html, body { width: 1200px; height: 948px; overflow: hidden; }
  body {
    background: var(--backdrop);
    font-family: "Arimo", Arial, sans-serif;
    position: relative;
  }
  .card {
    position: absolute;
    left: 240px;
    width: 720px;
    height: 411px;
    border-radius: 26px;
    overflow: hidden;
  }
  .card--front { top: 44px; background: var(--brand-blue); color: var(--paper); }
  .card--back { top: 493px; background: var(--paper); color: var(--ink); }

  .wordmark {
    position: absolute;
    display: flex;
    align-items: center;
    gap: 16px;
    font-weight: 700;
    line-height: 1.02;
    white-space: nowrap;
  }
  .wordmark__dot {
    width: 22px; height: 22px; border-radius: 50%;
    background: var(--brand-red);
    flex: none;
  }
  .card--front .wordmark { left: 150px; top: 70px; font-size: 46px; color: var(--paper); }
  .card--back .wordmark { left: 50px; top: 158px; font-size: 30px; color: var(--ink); gap: 14px; }
  .card--back .wordmark__dot { width: 18px; height: 18px; }

  .locations {
    position: absolute;
    left: 40px; right: 40px; bottom: 50px;
    display: flex;
    gap: 22px;
  }
  .location {
    flex: 1;
    font-size: 15.5px;
    line-height: 1.35;
    padding-left: 18px;
    border-left: 1.5px solid var(--brand-red);
    white-space: nowrap;
  }
  .location:first-child { border-left: none; padding-left: 0; }

  .divider {
    position: absolute;
    left: 372px; top: 70px;
    width: 1.5px; height: 236px;
    background: var(--brand-red);
  }
  .contact {
    position: absolute;
    left: 400px; top: 66px;
    font-size: 16px;
    line-height: 1.35;
  }
  .contact__name { font-size: 30px; font-weight: 700; line-height: 1.1; white-space: nowrap; }
  .contact__first { color: var(--brand-blue); }
  .contact__last { color: var(--brand-red); }
  .contact__title { margin-bottom: 14px; }
  .contact__address { margin-bottom: 14px; }
  .contact__row { display: flex; align-items: center; gap: 8px; }
  .contact__row svg { width: 14px; height: 14px; flex: none; }

  .band-rule {
    position: absolute; left: 0; right: 0; bottom: 28px;
    height: 2px; background: var(--brand-red);
  }
  .band {
    position: absolute; left: 0; right: 0; bottom: 0;
    height: 26px; background: var(--brand-blue);
  }
</style>
</head>
<body>

<section class="card card--front" aria-label="Card front">
  <div class="wordmark">
    <span class="wordmark__dot"></span>
    <span>Tallow Drug<br>&amp; Home Medical</span>
  </div>
  <div class="locations">
    <div class="location">
      Hampstead Commons<br>
      412 Pine Road Suite 8<br>
      Hampstead, NC 28443<br>
      Phone: 910-555-0118
    </div>
    <div class="location">
      Harbor Point<br>
      2650 Seabreeze Avenue<br>
      Wilmington, NC 28411<br>
      Phone: 910-555-0172
    </div>
    <div class="location">
      Jacksonville<br>
      391 Riverbend Lane<br>
      Jacksonville, NC 28540<br>
      Phone: 910-555-0196
    </div>
  </div>
</section>

<section class="card card--back" aria-label="Card back">
  <div class="wordmark">
    <span class="wordmark__dot"></span>
    <span>Tallow Drug<br>&amp; Home Medical</span>
  </div>
  <div class="divider"></div>
  <div class="contact">
    <div class="contact__name"><span class="contact__first">Derek</span> <span class="contact__last">Halvorsen</span></div>
    <div class="contact__title">Patient Liaison</div>
    <div class="contact__address">391 Riverbend Lane<br>Jacksonville, NC 28540</div>
    <div class="contact__row">
      <svg viewBox="0 0 24 24" aria-hidden="true"><path fill="#283593" d="M6.6 10.8a15.1 15.1 0 0 0 6.6 6.6l2.2-2.2a1 1 0 0 1 1-.25 11.4 11.4 0 0 0 3.6.57 1 1 0 0 1 1 1V20a1 1 0 0 1-1 1A17 17 0 0 1 3 4a1 1 0 0 1 1-1h3.5a1 1 0 0 1 1 1c0 1.25.2 2.450.57 3.57a1 1 0 0 1-.25 1z"/></svg>
      <span>910-555-0143</span>
    </div>
    <div class="contact__row">
      <svg viewBox="0 0 24 24" aria-hidden="true"><path fill="#283593" d="M3 5h18v14H3z"/><path fill="none" stroke="#fff" stroke-width="1.8" d="M3 5l9 8 9-8"/></svg>
      <span>Derek@tallowmedco.com</span>
    </div>
    <div class="contact__row">
      <svg viewBox="0 0 24 24" aria-hidden="true"><circle cx="12" cy="12" r="10" fill="#283593"/><path fill="none" stroke="#fff" stroke-width="1.4" d="M2 12h20M12 2c3 3 3 17 0 20M12 2c-3 3-3 17 0 20"/></svg>
      <span>www.tallowmedco.com</span>
    </div>
  </div>
  <div class="band-rule"></div>
  <div class="band"></div>
</section>

</body>
</html>
```